wooden jewelry - pearl necklaces

I sell wooden jeweler (rings and pearls) on markets, and so on. I also opened my business as a carpenter. The rings and a combination of wood and metal. The wood is special wood, not very common on Europe. I paint the rings afterwards. You can see some of the pictures on the pictures I uploaded. The pearls are made of the same kind of wood and colored in all kinds of colors. They are then assembled to bracelets. The jewelry is very individual and looks really cool and all kinds of people.

Target Market(s)

Young urban alternative with a sense of individuality

Contact Information for Business Card

Front:

Text:

„Kugelwerk“ (big)
„Lukas Fendrich“ (smaler)

Back
„KUGELWERK
Herstellung von individuellem Holz- und Modeschmuck

Lukas Fendrich
Tel: 017659324618
Mirowgasse 27
84492 Burghausen

lukasfendrich@mailhafen.de“

Font styles to use
Sans Serif

Requirements
Nice to have
• Nice to see a camel thorn tree on the background, this is a special wood and some of the rings are made out of this wood.

```html
<!DOCTYPE html>
<html lang="de">
<head>
<meta charset="utf-8">
<title>Kugelwerk – Visitenkarte</title>
<link rel="stylesheet" href="https://fonts.googleapis.com/css2?family=Jost:wght@600&family=Open+Sans:wght@400;700&display=swap">
<style>
  :root {
    --page: #ffffff;
    --ink-white: #ffffff;
    --panel-grey: #262626;
    --panel-black: #0c0c0c;
    --swoosh-grey: #2a2a2a;
    --bead-dark: #1a1519;
    --bead-mid: #2b2126;
    --bead-warm: #3a2a24;
  }
  * { margin: 0; padding: 0; box-sizing: border-box; }
  html, body { width: 1200px; height: 900px; overflow: hidden; background: var(--page); }
  .canvas { position: relative; width: 1200px; height: 900px; }

  .card {
    position: absolute;
    border-radius: 14px;
    overflow: hidden;
    color: var(--ink-white);
  }
  .bead-photo {
    position: absolute; inset: 0;
    background:
      radial-gradient(circle at 20% 30%, var(--bead-warm) 0%, transparent 45%),
      radial-gradient(circle at 75% 70%, var(--bead-warm) 0%, transparent 40%),
      linear-gradient(135deg, var(--bead-mid), var(--bead-dark));
  }

  /* Back side */
  .card-back { left: 290px; top: 90px; width: 568px; height: 324px; }
  .card-back .holder-name {
    position: absolute; left: 27px; top: 46px;
    font: 700 20px/1 "Open Sans", sans-serif; letter-spacing: 1px;
  }
  .card-back .brand-name {
    position: absolute; right: 30px; top: 58px;
    font: 700 22px/1 "Open Sans", sans-serif; letter-spacing: 1px;
  }
  .panel-phone {
    position: absolute; left: 0; top: 117px; width: 322px; height: 207px;
    background: var(--panel-grey); border-top-right-radius: 14px;
  }
  .panel-details {
    position: absolute; left: 0; top: 181px; width: 322px; height: 143px;
    background: var(--panel-black); border-top-right-radius: 22px;
  }
  .swoosh { position: absolute; left: 0; top: 0; }
  .contact-row {
    position: absolute; left: 28px; display: flex; align-items: center; gap: 12px;
    font: 400 13.5px/1.45 "Open Sans", sans-serif;
  }
  .contact-icon {
    width: 30px; height: 30px; border-radius: 50%; background: var(--ink-white);
    display: flex; align-items: center; justify-content: center; flex: none;
  }
  .row-phone { top: 132px; }
  .row-mail { top: 205px; }
  .row-address { top: 266px; }

  /* Front side */
  .card-front { left: 286px; top: 498px; width: 575px; height: 328px; }
  .front-title {
    position: absolute; left: 0; right: 0; top: 90px; text-align: center;
    font: 600 78px/1 "Jost", sans-serif; letter-spacing: 1px;
  }
  .front-name {
    position: absolute; left: 0; right: 0; top: 202px; text-align: center;
    font: 400 31px/1 "Open Sans", sans-serif; letter-spacing: 10px;
  }
</style>
</head>
<body>
<div class="canvas">

  <section class="card card-back">
    <div class="bead-photo" role="img" aria-label="Hintergrundfoto mit bunten Holzperlen, stark abgedunkelt"></div>
    <svg class="swoosh" width="568" height="324" viewBox="0 0 568 324" aria-hidden="true">
      <path d="M322 324 C 380 230, 470 180, 568 165 L568 324 Z" fill="var(--panel-black)"/>
      <path d="M336 324 C 390 245, 475 200, 568 190 L568 324 Z" fill="var(--swoosh-grey)"/>
    </svg>
    <div class="panel-phone"></div>
    <div class="panel-details"></div>

    <div class="holder-name">LUKAS FENDRICH</div>
    <div class="brand-name">KUGELWERK</div>

    <div class="contact-row row-phone">
      <span class="contact-icon">
        <svg width="16" height="16" viewBox="0 0 24 24"><path d="M6.6 10.8a15.1 15.1 0 0 0 6.6 6.6l2.2-2.2a1 1 0 0 1 1-.25 11.4 11.4 0 0 0 3.6.57 1 1 0 0 1 1 1V20a1 1 0 0 1-1 1A17 17 0 0 1 3 4a1 1 0 0 1 1-1h3.5a1 1 0 0 1 1 1c0 1.25.2 2.450 .57 3.57a1 1 0 0 1-.25 1Z" fill="#111"/></svg>
      </span>
      <span>017659324618</span>
    </div>
    <div class="contact-row row-mail">
      <span class="contact-icon">
        <svg width="16" height="16" viewBox="0 0 24 24"><rect x="3" y="6" width="18" height="12" rx="1.5" fill="#111"/><path d="M3.5 6.8 12 13l8.5-6.2" stroke="#fff" stroke-width="1.4" fill="none"/></svg>
      </span>
      <span>lukasfendrich@mailhafen.de</span>
    </div>
    <div class="contact-row row-address">
      <span class="contact-icon">
        <svg width="16" height="16" viewBox="0 0 24 24"><path d="M12 2a6 6 0 0 0-6 6c0 4.5 6 11 6 11s6-6.5 6-11a6 6 0 0 0-6-6Zm0 8.2A2.2 2.2 0 1 1 12 5.8a2.2 2.2 0 0 1 0 4.4Z" fill="#111"/><ellipse cx="12" cy="20.5" rx="6" ry="1.6" fill="none" stroke="#111" stroke-width="1.3"/></svg>
      </span>
      <span>Mirowgasse 27<br>84492 Tannfeld</span>
    </div>
  </section>

  <section class="card card-front">
    <div class="bead-photo" role="img" aria-label="Hintergrundfoto mit bunten Holzperlen, stark abgedunkelt"></div>
    <h1 class="front-title">Kugelwerk</h1>
    <p class="front-name">Lukas Fendrich</p>
  </section>

</div>
</body>
</html>
```